Create Homepage Header & Search Box for Education Website

This project is relatively small and pays well.
Site: brightlearnhub.org
Project Title:
Redesign slider to be a static image/graphic and include a 3 drop down search box.
Project Summary:
We need a new homepage header for brightlearnhub.org. The logo, top navigation, and social buttons should remain unchanged. The new header needs to include a static graphic or image and a 3 drop down search box. It can also include some text that speaks to the what our site provides. For text suggestions - see below. Placement for the search box should be to the left under the logo. We will remove the slider functionality and need the design to be static.
Below the current slider images are bar graphs and a pie graph. These can remain as is - or you can make design changes. If you make design changes - please be sure the message doesn't change. Also you can submit one version of the design with this removed if you feel like it helps best accomplish our goal of conversion.
Project Objectives:
The primary objective of the deign is to maximize conversion of clicks to the search box. We need users to gravitate to the search box. Additionally the design should convey trust and academic feel.
Target Market:
High School Graduates and people in their 20s looking for college options.
Potential text:
Tagline Option: "Your #1 Resource for an Affordable Online College Education"
Tagline Option: "Find Affordable Online College Options"
Other Details: Brightlearn Study Hub will help you find a more affordable college experience. Look no further to find financial aid information, cost saving tips, and comprehensive college rankings focused on affordability and value.
Or you can also use some placeholder text and I can create the right messaging.
The Search Box:
The search box is pretty standard - you can see examples in the examples below - or in the files I attached. 3 drop downs and a "Search" button.
Examples of some previous designs attached to the project:
These designs are close - but not perfect. These will give you a good general idea for what we need.
Examples of designs at similar websites:
kvrt.org
campusmeadow.net
toplecternest.com

```html
<!DOCTYPE html>
<html lang="en">
<head>
<meta charset="utf-8">
<title>Brightlearn Study Hub</title>
<link rel="stylesheet" href="https://fonts.googleapis.com/css2?family=Arimo:wght@400;700&family=Open+Sans:wght@300;400&family=Oswald:wght@400;500&display=swap">
<style>
:root{
  --orange:#f26b38;
  --orange-deep:#ff5a00;
  --amber:#ffc000;
  --navy:#1b2029;
  --teal:#0f5a5a;
  --teal-dark:#0b3a40;
  --lime:#a8c83a;
  --ink:#222;
  --grey:#777;
  --sky:#c9eefa;
  --white:#fff;
}
*{box-sizing:border-box;margin:0;padding:0}
html,body{width:1200px;height:1131px;overflow:hidden;background:var(--white);font-family:"Arimo",Arial,sans-serif;color:var(--ink)}
.page{position:relative;width:1200px;height:1131px}

/* top bar */
.brand{position:absolute;left:100px;top:14px;display:flex;align-items:center;gap:10px}
.brand-dot{width:46px;height:46px;border-radius:50%;background:var(--orange)}
.brand-name{font-family:"Open Sans",sans-serif;font-weight:400;color:var(--orange);font-size:15px;line-height:18px;width:100px}
.nav a{position:absolute;top:28px;font-family:"Open Sans",sans-serif;font-size:18px;color:#333;text-decoration:none}
.nav a.active{color:var(--orange);border-bottom:1px solid var(--orange);padding-bottom:1px}
.social span{position:absolute;top:29px;width:24px;height:24px;border-radius:4px}
.social .s1{left:996px;background:#3b5998}
.social .s2{left:1033px;background:#1da1f2}
.social .s3{left:1073px;background:#dd4b39}

/* hero */
.hero{position:absolute;left:0;top:77px;width:1200px;height:339px;
  background:radial-gradient(ellipse at 25% 10%,#f4fcff 0%,transparent 45%),linear-gradient(90deg,#bfeaf8 0%,#e2f6fd 45%,#ffffff 75%)}
.hero h1{position:absolute;left:87px;top:118px;font-size:25px;font-weight:700;color:var(--ink)}
.hero p{position:absolute;left:87px;top:155px;width:650px;font-size:15px;line-height:21.5px;color:#333}

.search{position:absolute;left:843px;top:89px;width:320px;height:320px;background:linear-gradient(90deg,var(--orange-deep),var(--amber))}
.search-tab{position:absolute;left:828px;top:102px;width:340px;height:52px}
.search-tab .get{position:absolute;left:40px;top:8px;font-family:"Oswald",sans-serif;font-size:13px;line-height:20px;color:#fff}
.search-tab .big{position:absolute;left:115px;top:2px;font-size:27px;font-weight:700;color:#fff}
.search-tab .small{position:absolute;left:117px;top:34px;font-size:11.5px;font-weight:700;color:#fff}
.field{position:absolute;left:875px;width:259px;height:43px;display:flex;box-shadow:0 2px 2px rgba(0,0,0,.25)}
.field .num{width:47px;background:var(--lime);font-size:25px;display:flex;align-items:center;justify-content:center;color:#222}
.field .select{flex:1;background:linear-gradient(#fff,#ececec);display:flex;align-items:center;justify-content:space-between;padding:0 12px 0 12px;font-size:15px;color:#444}
.field .arrows{display:flex;align-items:center;gap:8px;border-left:1px solid #ccc;padding-left:8px;height:18px}
.btn-search{position:absolute;left:901px;top:348px;width:205px;height:46px;border-radius:8px;background:linear-gradient(#104a50,#0a2a30);color:#fff;font-size:26px;font-weight:700;display:flex;align-items:center;justify-content:center}

/* stats band */
.stats{position:absolute;left:0;top:416px;width:1200px;height:116px;background:var(--navy)}
.bar{position:absolute;left:104px;width:172px;height:39px;border:1px solid #333a44}
.bar .fill{position:absolute;left:0;top:0;bottom:0;background:var(--teal);color:#fff;font-family:"Oswald",sans-serif;font-size:26px;line-height:37px;padding-left:14px;white-space:nowrap}
.bar-label{position:absolute;left:295px;font-family:"Oswald",sans-serif;font-weight:500;font-size:20px;color:var(--orange);letter-spacing:-.5px}
.pie{position:absolute;left:599px;top:426px}
.stats h2{position:absolute;left:716px;top:430px;font-family:"Open Sans",sans-serif;font-weight:400;font-size:17px;color:var(--orange)}
.stats p{position:absolute;left:714px;top:458px;width:350px;text-align:center;font-size:12.5px;line-height:18px;color:#fff}

/* feature cards */
.card{position:absolute;width:320px;display:flex;gap:15px}
.card .icon{flex:none;width:80px;height:80px;border-radius:50%;background:var(--orange);display:flex;align-items:center;justify-content:center}
.card .body{width:212px;padding-top:4px}
.card h3{font-family:"Open Sans",sans-serif;font-weight:400;font-size:17px;line-height:22px;color:#333}
.card p{margin-top:13px;font-size:12.5px;line-height:21px;color:var(--grey)}
.card .more{display:flex;justify-content:flex-end;margin-top:6px}
.card .more a{border:1px solid #ddd;padding:3px 10px;font-size:11.5px;color:#c0392b;text-decoration:none}
</style>
</head>
<body>
<div class="page">

  <header>
    <div class="brand"><span class="brand-dot"></span><span class="brand-name">Brightlearn Study Hub</span></div>
    <nav class="nav">
      <a style="left:266px">Home</a>
      <a class="active" style="left:356px">Financial Aid</a>
      <a style="left:503px">Cost Savings</a>
      <a style="left:654px">Colleges</a>
      <a style="left:767px">Awards</a>
      <a style="left:872px">Blog</a>
    </nav>
    <div class="social" aria-label="Social links"><span class="s1"></span><span class="s2"></span><span class="s3"></span></div>
  </header>

  <section class="hero" role="img" aria-label="Soft light-blue sunburst background">
    <h1>Resource for an Affordable Online College Education</h1>
    <p>Brightlearn Study Hub will help you find a more affordable college experience. Look no further to find financial aid information, cost saving tips, and comprehensive college rankings focused on affordability and value.</p>
  </section>

  <aside>
    <div class="search"></div>
    <div class="search-tab">
      <svg width="340" height="52" style="position:absolute;left:0;top:0">
        <path d="M12 0 H340 L328 52 H12 Q0 52 0 40 V12 Q0 0 12 0Z" fill="#0c1418"/>
        <path d="M105 0 H340 L328 52 H105Z" fill="#1aa0c8"/>
        <path d="M105 0 H340 L334 26 H105Z" fill="#35b8dc"/>
      </svg>
      <div class="get">GET<br>INFO!</div>
      <div class="big">SEARCH HERE</div>
      <div class="small">REQUEST MORE INFORMATION</div>
    </div>
    <div class="field" style="top:184px"><span class="num">1</span><span class="select">Choose a Degree Level<span class="arrows"><svg width="12" height="18"><path d="M6 1 L11 7 H1Z M6 17 L11 11 H1Z" fill="#5a8f2a"/></svg></span></span></div>
    <div class="field" style="top:237px"><span class="num">2</span><span class="select">Choose a Category<span class="arrows"><svg width="12" height="18"><path d="M6 1 L11 7 H1Z M6 17 L11 11 H1Z" fill="#5a8f2a"/></svg></span></span></div>
    <div class="field" style="top:290px"><span class="num">3</span><span class="select">Choose a Subject<span class="arrows"><svg width="12" height="18"><path d="M6 1 L11 7 H1Z M6 17 L11 11 H1Z" fill="#5a8f2a"/></svg></span></span></div>
    <div class="btn-search">Search Now</div>
  </aside>

  <section class="stats">
    <div class="bar" style="top:10px"><div class="fill" style="width:97px">$12,500</div></div>
    <div class="bar" style="top:62px"><div class="fill" style="width:143px">$26,600</div></div>
    <div class="bar-label" style="top:15px">AVERAGE STUDENT DEBT IN 1996</div>
    <div class="bar-label" style="top:67px">AVERAGE STUDENT DEBT IN 2011</div>
    <svg class="pie" width="90" height="90" style="top:10px">
      <circle cx="45" cy="45" r="44" fill="var(--teal)"/>
      <path d="M45 45 L45 1 A44 44 0 0 1 87 57 Z" fill="#0e141b"/>
      <text x="45" y="55" text-anchor="middle" font-family="Oswald,sans-serif" font-size="26" fill="#fff">66%</text>
    </svg>
    <h2 style="top:14px">College Costs Rising &amp; Student Debt Ballooning</h2>
    <p style="top:42px">Brightlearn Study Hub helps students find affordable college options and provides information about financial aid and college rankings.</p>
  </section>

  <main>
    <div class="card" style="left:103px;top:583px">
      <div class="icon"><svg width="40" height="52"><text x="20" y="44" text-anchor="middle" font-family="Arimo,sans-serif" font-weight="700" font-size="50" fill="#fff">$</text></svg></div>
      <div class="body"><h3>Financial Aid</h3><p>The nuts of bolts of financial aid – what's available and how to apply.</p><div class="more"><a>Read more</a></div></div>
    </div>
    <div class="card" style="left:440px;top:583px">
      <div class="icon"><svg width="56" height="44"><rect x="2" y="32" width="8" height="12" fill="#fff"/><rect x="16" y="24" width="8" height="20" fill="#fff"/><rect x="30" y="16" width="8" height="28" fill="#fff"/><rect x="44" y="8" width="8" height="36" fill="#fff"/><path d="M2 26 L18 16 L30 18 L52 2" stroke="#fff" stroke-width="3" fill="none"/></svg></div>
      <div class="body"><h3>Rising College Costs: Who is Helping?</h3><p>Who's helping and what does that mean for you?</p><div class="more"><a>Read more</a></div></div>
    </div>
    <div class="card" style="left:777px;top:583px">
      <div class="icon"><svg width="56" height="44"><ellipse cx="28" cy="22" rx="24" ry="17" fill="#fff"/><rect x="14" y="34" width="7" height="9" fill="#fff"/><rect x="34" y="34" width="7" height="9" fill="#fff"/><text x="26" y="28" text-anchor="middle" font-family="Arimo,sans-serif" font-weight="700" font-size="16" fill="var(--orange)">$</text></svg></div>
      <div class="body"><h3>Affordability Tips</h3><p>Check out our tips for how you can make college more affordable</p><div class="more"><a>Read more</a></div></div>
    </div>

    <div class="card" style="left:103px;top:798px">
      <div class="icon"><svg width="48" height="44"><path d="M24 2 L46 12 H2Z" fill="#fff"/><rect x="4" y="14" width="40" height="3" fill="#fff"/><rect x="8" y="19" width="5" height="18" fill="#fff"/><rect x="17" y="19" width="5" height="18" fill="#fff"/><rect x="26" y="19" width="5" height="18" fill="#fff"/><rect x="35" y="19" width="5" height="18" fill="#fff"/><rect x="2" y="39" width="44" height="4" fill="#fff"/></svg></div>
      <div class="body"><h3>Affordable Campus Colleges</h3><p>Which colleges offer the best value?</p><div class="more"><a>Read more</a></div></div>
    </div>
    <div class="card" style="left:440px;top:798px">
      <div class="icon"><svg width="50" height="60"><circle cx="25" cy="22" r="18" fill="none" stroke="#fff" stroke-width="3"/><circle cx="25" cy="22" r="11" fill="none" stroke="#fff" stroke-width="2"/><path d="M15 37 L9 56 L16 52 L20 58 L25 40 M35 37 L41 56 L34 52 L30 58 L25 40" stroke="#fff" stroke-width="2.5" fill="none"/></svg></div>
      <div class="body"><h3>Awards</h3><p>Awesome professors and financial aid folks working to make your life easier.</p><div class="more"><a>Read more</a></div></div>
    </div>
    <div class="card" style="left:777px;top:798px">
      <div class="icon"><svg width="52" height="44"><path d="M2 4 H30 V22 H14 L7 29 V22 H2Z" fill="#fff"/><path d="M20 14 H50 V32 H46 V40 L38 32 H20Z" fill="#fff" stroke="var(--orange)" stroke-width="2"/></svg></div>
      <div class="body"><h3>Blog</h3><p>The latest on making college affordable.</p><div class="more"><a>Read more</a></div></div>
    </div>

    <div class="card" style="left:103px;top:991px">
      <div class="icon"><svg width="52" height="48"><path d="M26 4 L50 14 L26 24 L2 14Z" fill="#fff"/><path d="M12 19 V30 Q26 38 40 30 V19 L26 25Z" fill="#fff"/><path d="M8 16 V34" stroke="#fff" stroke-width="2"/><ellipse cx="34" cy="40" rx="6" ry="7" fill="none" stroke="#fff" stroke-width="2"/></svg></div>
      <div class="body"><h3>Affordable Online Colleges</h3><p>Find affordable online colleges that offer great value to students.</p><div class="more"><a>Read more</a></div></div>
    </div>
    <div class="card" style="left:440px;top:991px">
      <div class="icon"><svg width="56" height="44"><rect x="10" y="6" width="36" height="26" fill="none" stroke="#fff" stroke-width="3"/><path d="M2 36 H54 L50 41 H6Z" fill="#fff"/></svg></div>
      <div class="body"><h3>College Classes Online</h3><p>Find introductory (101) college level classes offered free by top colleges</p><div class="more"><a>Read more</a></div></div>
    </div>
  </main>

</div>
</body>
</html>
```